Verdant Hollow Kukui Oil Label

We’re looking for a designer to develop a new label for our bottled Kukui oil. Final design files (including original file) would be provided to Verdant Hollow to make versions and updates as needed.

The label will be applied to a 4 ounce light amber PET Pavo round bottle (with a white disc top cap). Specs, content to include and more direction are provided in the provided brief.

Target Market(s)

Women and men, ages 25-49, who care about their skin and know what they do now is going to affect their skin as they age. They care about using natural products and want to know the ingredients. They’re aware of harmful ingredients (like parabens and phthalates), and if they aren’t aware, they want to be informed.

Their focus is on the overall value and experience provided by the product.

Industry/Entity Type

Skin Care Product

Font styles to use
Serif

Colors

Designer to choose colors to be used in the design.

Requirements
Must have
• The goal is to look simple and classic, and cater to men and women.
• Include the Verdant Hollow logo (either vertical or horizontal version)
• A UPC Code must be added to the box (location can be on the back lower corner). The size is 1.5 inches wide by .5 inches high. A code will be provided once a design draft is reviewed, since an annual cost will incur once a code is purchased.
• Messaging Requirements for label:
• Product Name:
• Kukui Oil
• Focal Point/Key Message:
• A superior moisturizer for the body, face and hair
• Include ingredients listing using a font size no less than 1/16” in height:
• Ingredients: Cold pressed kukui oil (aleurites moluccana), Vitamin E and phthalate-free lime fragrance.
•  
• List the product amount:
• 4.0 fl. oz. / 118 mL
• Include Directions for Use after or near Ingredients listing:
• Directions for Use: Apply a few drops as needed to your body, face or hair.
• Include Warnings after Directions. Lettering must be in bold type and in all CAPS on white background and may in no case be less than 1/16 inch in height:
• Warnings: For external use only. not recommended for those with nut allergies. Use as directed. Avoid contact with eyes. Keep out of reach of children.
• Include Website and contact info:
• VerdantHollow.com
• MADE IN U.S.A.
• Produced and distributed by Verdant HollowTM
• Marlow Falls, Ohio 43999
• Promotional copy to include:
• Kukui oil is widely used by the Hawaiian surfing community to help heal cuts, scrapes and sunburns. With high levels of linoleic and alpha-linolenic acids, this light oil deeply penetrates the skin’s tissues without leaving a greasy film.
• Other uses: An everyday moisturizer. Treats eczema and psoriasis. Removes make-up.
• (If this is too much copy, I can try and shorten the Promotional Copy and Other Uses sections)
Nice to have
• The flower from the logo represents “natural beauty” and we currently use it on its own and incorporate it as a design element. We’re open to enhancing the flower, using it in different ways or not using it on its own at all.
• Our current Website branding may be leveraged (verdanthollow.com):
• Font Family:
• Quattrocento (Normal 400)
• Back-up Font Family:
• Verdana, Geneva sans
• Headline color:
• Black #333333
• Body copy color:
• Gray #747474
Should not have
• What we don’t want:
• Too many colors
• Overly bright colors
• Photography

```html
<!DOCTYPE html>
<html lang="en">
<head>
<meta charset="utf-8">
<title>Verdant Hollow Kukui Oil Label</title>
<link rel="stylesheet" href="https://fonts.googleapis.com/css2?family=Quattrocento:wght@400;700&family=Open+Sans:wght@400;700&display=swap">
<style>
  :root {
    --ink: #2b2b2b;
    --body-gray: #747474;
    --label-gray: #8a8a8a;
    --teal: #0b86a0;
    --sun: #f5de72;
    --blush: #f2c9c3;
    --blush-soft: #f8e1df;
    --rule-gray: #cfcfcf;
    --paper: #ffffff;
  }
  * { margin: 0; padding: 0; box-sizing: border-box; }
  html, body { width: 1200px; height: 999px; overflow: hidden; background: var(--paper); }
  .canvas { position: relative; width: 1200px; height: 999px; }

  /* back panel */
  .promo-box {
    position: absolute; left: 146px; top: 188px; width: 246px; height: 163px;
    background: var(--sun); padding: 15px 19px;
    font: 400 13.2px/1.34 "Quattrocento", serif; color: var(--ink); text-align: justify;
  }
  .usage { position: absolute; left: 164px; top: 405px; width: 209px; font-family: "Open Sans", sans-serif; }
  .usage h3 { font-size: 10.5px; font-weight: 700; color: var(--ink); line-height: 1.2; }
  .usage p { font-size: 10.5px; color: var(--label-gray); line-height: 1.25; text-align: justify; }
  .usage .warning-text { text-transform: uppercase; letter-spacing: 0.6px; }
  .usage .block + .block { margin-top: 16px; }
  .maker {
    position: absolute; left: 164px; top: 697px; width: 220px;
    font: 700 10.5px/1.3 "Open Sans", sans-serif; color: var(--label-gray);
  }
  .maker p + p { margin-top: 13px; }

  /* front panel */
  .panel-edge { position: absolute; top: 140px; width: 1px; height: 718px; background: var(--rule-gray); }
  .panel-edge.left { left: 430px; }
  .panel-edge.right { left: 676px; }
  .front-frame {
    position: absolute; left: 443px; top: 140px; width: 220px; height: 687px;
    border: 2px solid var(--teal); border-top: none;
  }
  .brand {
    position: absolute; left: 443px; top: 214px; width: 220px; text-align: center;
    font: 400 22px/1 "Quattrocento", serif; color: var(--teal); letter-spacing: 0.5px;
  }
  .brand-dot { display: inline-block; width: 9px; height: 9px; border-radius: 50%; background: var(--blush); margin-left: 6px; vertical-align: middle; }
  .motif { position: absolute; left: 463px; top: 400px; width: 175px; height: 175px; }
  .product-name {
    position: absolute; left: 430px; top: 420px; width: 246px; text-align: center;
    font: 400 60px/1.02 "Quattrocento", serif; color: var(--ink);
  }
  .tagline-band {
    position: absolute; left: 430px; top: 651px; width: 246px; height: 62px;
    background: var(--sun); display: flex; align-items: center; justify-content: center; text-align: center;
    font: 700 11px/1.3 "Quattrocento", serif; color: var(--ink); letter-spacing: 0.3px;
  }
  .net-contents {
    position: absolute; left: 430px; top: 832px; width: 246px; text-align: center;
    font: 400 14px/1 "Quattrocento", serif; color: var(--ink);
  }

  /* base stripes */
  .stripe-blush { position: absolute; left: 122px; top: 866px; width: 576px; height: 7px; background: var(--blush); }
  .stripe-teal { position: absolute; left: 122px; top: 873px; width: 576px; height: 26px; background: var(--teal); }
</style>
</head>
<body>
<main class="canvas">
  <section class="back-panel">
    <p class="promo-box">Kukui nut oil is widely used by the Hawaiian surfing community to help heal cuts, scrapes and sunburns. With high levels of linoleic and alpha-linolenic acids, this light oil deeply penetrates the skin’s tissues without leaving a greasy film.</p>
    <div class="usage">
      <div class="block">
        <h3>Directions for Use:</h3>
        <p>Apply a few drops as needed to your body, face or hair.</p>
      </div>
      <div class="block">
        <h3>WARNINGS:</h3>
        <p class="warning-text">For external use only. Not recommended for those with nut allergies. Use as directed. Avoid contact with eyes. Keep out of reach of children.</p>
      </div>
    </div>
    <div class="maker">
      <p>MADE IN U.S.A.</p>
      <p>Produced and distributed by Verdant HollowTM Marlow Falls, Ohio 43999</p>
      <p>VerdantHollow.com</p>
    </div>
  </section>

  <section class="front-panel">
    <div class="panel-edge left"></div>
    <div class="panel-edge right"></div>
    <div class="front-frame"></div>
    <div class="brand">Verdant Hollow<span class="brand-dot"></span></div>
    <svg class="motif" viewBox="0 0 175 175" role="img" aria-label="Faint flower motif behind the product name">
      <defs>
        <radialGradient id="motifGlow" cx="50%" cy="50%" r="50%">
          <stop offset="0%" stop-color="#f8e1df" stop-opacity="0.9"/>
          <stop offset="100%" stop-color="#f8e1df" stop-opacity="0"/>
        </radialGradient>
      </defs>
      <circle cx="87.5" cy="87.5" r="87.5" fill="url(#motifGlow)"/>
    </svg>
    <h1 class="product-name">Kukui<br>Oil</h1>
    <p class="tagline-band">A SUPERIOR MOISTURIZER<br>FOR THE BODY, FACE AND HAIR</p>
    <p class="net-contents">4.0 fl. oz. / 118 mL</p>
  </section>

  <div class="stripe-blush"></div>
  <div class="stripe-teal"></div>
</main>
</body>
</html>
```